Vireon Spool Business Card Design

This is a start up company that has state of the art patented technology for turbo chargers,that can be used on engines, gas or diesel, for any type of automotive,aviation,marine or industrial purpose.
This technology will provide longer life,lower maintenance and better performance and help produce lower emissions with any turbocharged engine.Red would be a predominate color and the design should communicate the latest technology,economy and
Environmental concern.
This product will initially be distributed in the U.S.A. But should move rapidly to global use.
Updates

Thank you for your design submissions, I have increased the budget for this job because my initial order was too low for the quality of work shown, plus I would Like to see some more options. I have a meeting this Sunday with my other partners and would anticipate being able to give you some feedback by the Beginning of next week. Regards.

Thank you for everyone's participation. The deadline is still open until 6/15 and my partners and I have a meeting Scheduled this weekend. At this time we have not ruled anyone out, But will be making a decision during the course of our meeting and wil Decide which direction we will be going in by the beginning of the week. Thanks again, regards, Tom Brandt.

Hello everybody, Sorry for the delay in communication, we have been very busy in putting the start up together. We are still not decided on the design of the business card and have a wide range to choose from. I would anticipated we shall have an answer within the next two weeks. Regards, Tom Brandt.

Target Market(s)

Manufacturers and wholesalers' of OEM and replacement turbochargers

Industry/Entity Type

Industrial

Contact Information for Business Card

We need a logo that should incorporate the " Vireon, a " possibly super imposed over a turbo charger with the fan blades of the turbocharger showing in the center of the "a" .
Name,title,phone number and email address only, no street/mailing address at this time.
The full name of the company is
" Vireon Spool Dynamics LLC "
For the initial card you can use my info.
Thomas Brandt
VP Sales & Marketing
tbrandt@vireonspooldyn.example
555 014 2286

Requirements
Must have
• The Vireon A, the outline of a turbo charger
Nice to have
• Something classy and simple and worldly (global)
Should not have
• No engines,cars,boats,planes

```html
<!DOCTYPE html>
<html lang="en">
<head>
<meta charset="utf-8">
<title>Vireon Spool Dynamics – Business Card</title>
<link rel="stylesheet" href="https://fonts.googleapis.com/css2?family=Arimo:wght@400;700&display=swap">
<style>
  :root {
    --backdrop: #e9e6e1;
    --maroon: #6a0f14;
    --maroon-deep: #550a0e;
    --paper: #ffffff;
    --mist: #e6e4e4;
    --ink: #222222;
    --muted: #555555;
  }
  * { margin: 0; padding: 0; box-sizing: border-box; }
  html, body {
    width: 1200px;
    height: 800px;
    overflow: hidden;
    background: var(--backdrop);
    font-family: "Arimo", Arial, sans-serif;
  }
  .sheet {
    width: 1200px;
    height: 800px;
    display: flex;
    align-items: center;
    justify-content: center;
    gap: 40px;
  }
  .card {
    position: relative;
    width: 540px;
    height: 309px;
    overflow: hidden;
    box-shadow: 0 6px 18px rgba(0,0,0,0.18);
  }
  .card-front { background: linear-gradient(135deg, var(--maroon) 0%, var(--maroon-deep) 100%); }
  .card-back { background: var(--paper); }

  .brand-field {
    position: absolute;
    left: -50px;
    top: 110px;
    width: 360px;
    height: 290px;
    border-radius: 50%;
  }
  .card-front .brand-field { background: var(--mist); }
  .card-back .brand-field { background: var(--maroon); }

  .company-name {
    position: absolute;
    top: 34px;
    right: 30px;
    font-size: 24px;
    font-weight: 400;
    color: var(--mist);
    letter-spacing: 0.2px;
  }

  .contact {
    position: absolute;
    top: 56px;
    left: 300px;
  }
  .contact-name {
    font-size: 17px;
    font-weight: 700;
    color: var(--maroon);
  }
  .contact-title {
    font-size: 11px;
    color: var(--ink);
    margin-top: 2px;
  }
  .contact-lines {
    list-style: none;
    margin-top: 24px;
    font-size: 11px;
    color: var(--muted);
  }
  .contact-lines li {
    display: flex;
    align-items: center;
    gap: 7px;
    margin-bottom: 5px;
  }
  .contact-lines svg { width: 11px; height: 11px; flex: none; }
</style>
</head>
<body>
  <main class="sheet">
    <section class="card card-front" aria-label="Card front">
      <div class="brand-field" role="img" aria-label="Large brand letter mark in light grey"></div>
      <p class="company-name">Vireon Spool Dynamics LLC</p>
    </section>

    <section class="card card-back" aria-label="Card back">
      <div class="brand-field" role="img" aria-label="Large brand letter mark in maroon"></div>
      <div class="contact">
        <h1 class="contact-name">Thomas Brandt VP</h1>
        <p class="contact-title">Sales &amp; Marketing</p>
        <ul class="contact-lines">
          <li>
            <svg viewBox="0 0 24 24" aria-hidden="true"><path fill="#6a0f14" d="M6.6 10.8a15.1 15.1 0 0 0 6.6 6.6l2.2-2.2a1 1 0 0 1 1-.25 11.4 11.4 0 0 0 3.6.57 1 1 0 0 1 1 1V20a1 1 0 0 1-1 1A17 17 0 0 1 3 4a1 1 0 0 1 1-1h3.5a1 1 0 0 1 1 1c0 1.25.2 2.45.57 3.57a1 1 0 0 1-.25 1z"/></svg>
            <span>555.014.2286</span>
          </li>
          <li>
            <svg viewBox="0 0 24 24" aria-hidden="true"><rect x="2" y="5" width="20" height="14" fill="#6a0f14"/><path d="M2 5l10 8 10-8" fill="none" stroke="#ffffff" stroke-width="1.6"/></svg>
            <span>tbrandt@vireonspooldyn.example</span>
          </li>
        </ul>
      </div>
    </section>
  </main>
</body>
</html>
```